Commercial Real Estate Company Needs an Awesome Flyer Design for their Oceanfront Property

We need a 2-page flyer or our Class A Oceanfront Property in Santa Monica, California. Approximately 16,149 square feet of Class A rare oceanfront office space with private balconies will be in available 4th Quarter of 2014. The SPACE has not been on the market for over 20 YEARS!

I attached our Previous 2-page flyer for the 2,353 square feet. We need a new vibrant, modern flyer that will attract Tech, Entertainment, Financial, and Marketing Companies to our building. Also, the 2nd Floor Space Plan is attached.

Also, please check out our website www.verlindeproperty.com. We would like to use the colors of our website and logo to incorporate with the flyer.

I updated the Must Have's on the Listing!

Target Market(s)

Entertainment, Financial, Tech Companies

Industry/Entity Type

Real Estate

Requirements
Must have
• Our Company Logo, Company, Leasing Agents On the First and 2nd Page

Trevor L. Ashdown (310) 555-0142
trev@verlindeproperty.com

Mark Oda (310) 555-0187
mark@verlindeproperty.com

Verlinde Property.
5127 N Harlow Ave, Suite 210
West Hollywood, Ca. 90069
(310) 555-0142
www.verlindeproperty.com

Also, the Front Page should indicate

"Rare Class A Oceanfront Office Space in the heart of Santa Monica"
"2nd Floor Office Space consisting of 16,159 square feet with private balconies."
Nice to have
• Please use description of the office building. You can omit whatever you think is unnecessary

"Bellhaven Court is one of Santa Monica's rare commercial properties that is both strategically located in the city's burgeoning central business district, yet ideally positioned on palm-lined Ocean Ave directly across from the Pacific Ocean. Built in 1987, the 3-story mixed-use commercial and retail property features prestigious retail Tenants such as Kelp Tavu and Dune Kitchen."

"A year-round coastal Mediterranean climate, a highly diverse business sector, and the vibrant, pedestrian-oriented Linden Row Walkway and Harbor Crest Arcade makes this beachside community a highly desirable commercial and retail location."

```html
<!DOCTYPE html>
<html lang="en">
<head>
<meta charset="utf-8">
<title>Bellhaven Court Flyer</title>
<link rel="stylesheet" href="https://fonts.googleapis.com/css2?family=Federo&family=Lato:wght@400;700&family=Pinyon+Script&display=swap">
<style>
:root{
  --gold:#fdd325;
  --ink:#231f20;
  --title-gold:#f5cf2a;
  --navy:#15213f;
  --white:#ffffff;
  --bg:#ffffff;
}
*{box-sizing:border-box;margin:0;padding:0}
html,body{width:1200px;height:792px;overflow:hidden;background:var(--bg)}
body{position:relative;font-family:"Lato",sans-serif;color:var(--navy)}
.page{position:absolute;top:12px;width:543px;height:768px;background:var(--gold);overflow:hidden}
.page--front{left:38px}
.page--back{left:617px}
.abs{position:absolute}
.photo{position:absolute}
.brand-bar{position:absolute;left:0;width:543px;background:var(--ink)}
.brand-title{position:absolute;left:0;right:0;text-align:center;font-family:"Federo",sans-serif;color:var(--title-gold);font-size:33px;letter-spacing:1px}
.logo-tile{position:absolute;width:50px;height:46px;background:var(--white);display:flex;flex-direction:column;align-items:center;justify-content:center;font-family:"Lato",sans-serif;color:var(--ink);font-weight:700;font-size:7px;letter-spacing:.6px;line-height:1.25;text-align:center}
.script-head{position:absolute;left:0;right:0;top:414px;text-align:center;font-family:"Pinyon Script",cursive;font-size:60px;color:var(--navy);white-space:nowrap}
.callout{position:absolute;background:var(--ink);color:var(--gold);font-size:11.5px;display:flex;align-items:center;justify-content:center;white-space:nowrap}
.agents{position:absolute;left:191px;top:650px;width:197px;text-align:center;color:var(--ink)}
.agents h3{font-weight:400;font-size:11px;margin-top:27px;margin-bottom:6px}
.agents p{font-size:7.2px;line-height:1.45}
.agents .gap{margin-top:9px}
.frame{position:absolute;background:var(--white)}
.tab{position:absolute;left:34px;width:196px;height:22px}
.tab svg{position:absolute;left:0;top:0}
.tab span{position:absolute;left:41px;top:3px;font-size:13px;color:var(--gold)}
.body-copy{position:absolute;left:34px;width:218px;font-size:8.6px;line-height:1.38;text-align:justify;color:var(--navy)}
.bullets{position:absolute;list-style:none;font-size:8.4px;color:var(--navy)}
.bullets li{position:relative;padding-left:26px}
.bullets li::before{content:"";position:absolute;left:6px;top:2px;width:7px;height:7px;background:var(--ink);clip-path:polygon(50% 0,62% 30%,100% 20%,72% 50%,100% 80%,62% 70%,50% 100%,38% 70%,0 80%,28% 50%,0 20%,38% 30%)}
.contact{position:absolute;left:0;top:634px;width:366px;height:134px;background:var(--ink);color:var(--gold);padding:9px 34px}
.contact h3{font-weight:400;font-size:11.5px}
.contact p{font-size:7.2px;line-height:1.45}
.contact .gap{margin-top:6px}
</style>
</head>
<body>

<section class="page page--front" aria-label="Front page">
  <div class="brand-bar" style="top:0;height:8px"></div>
  <div class="photo" role="img" aria-label="Photo of the three-story white building on a palm-lined street under blue sky" style="left:0;top:8px;width:543px;height:302px;background:linear-gradient(180deg,#2e5fb0 0%,#6e97cf 30%,#d9d6cf 55%,#cfcac2 75%,#4d4f57 88%,#8a8b8e 100%)"></div>
  <div class="brand-bar" style="top:310px;height:68px">
    <div class="logo-tile" style="left:11px;top:11px">VERLINDE<br>PROPERTY</div>
    <div class="brand-title" style="top:15px">BELLHAVEN COURT</div>
    <div class="logo-tile" style="right:11px;top:11px">VERLINDE<br>PROPERTY</div>
  </div>
  <div class="script-head">Prestigious Workplace</div>
  <div class="callout" style="left:87px;top:515px;width:369px;height:28px">"Rare Class A Oceanfront Office Space in the heart of Santa Monica"</div>
  <div class="callout" style="left:56px;top:558px;width:431px;height:28px">"2nd Floor Office Space consisting of 16,159 square feet with private balconies."</div>
  <div class="frame" style="left:0;top:636px;width:195px;height:132px"></div>
  <div class="photo" role="img" aria-label="Photo of an empty office with windows overlooking palms" style="left:0;top:642px;width:189px;height:126px;background:linear-gradient(160deg,#cfd3d6 0%,#e5e2dc 45%,#8c8275 100%)"></div>
  <div class="agents">
    <h3>Our Leasing Agents :</h3>
    <p>Trevor L. Ashdown (310) 555-0142<br>trev@verlindeproperty.com</p>
    <p class="gap">Mark Oda (310) 555-0187<br>mark@verlindeproperty.com</p>
  </div>
  <div class="frame" style="left:348px;top:636px;width:195px;height:132px"></div>
  <div class="photo" role="img" aria-label="Photo of an office interior with a curved wooden reception desk" style="left:353px;top:642px;width:190px;height:126px;background:linear-gradient(180deg,#e8e6e0 0%,#cdc7bc 50%,#b78a4e 80%,#9c8a72 100%)"></div>
</section>

<section class="page page--back" aria-label="Back page">
  <div class="brand-bar" style="top:0;height:66px">
    <div class="logo-tile" style="left:11px;top:10px">VERLINDE<br>PROPERTY</div>
    <div class="brand-title" style="top:12px">BELLHAVEN COURT</div>
    <div class="logo-tile" style="right:11px;top:10px">VERLINDE<br>PROPERTY</div>
  </div>

  <div class="tab" style="top:98px">
    <svg width="196" height="22" viewBox="0 0 196 22"><rect x="0" y="0" width="25" height="22" fill="#231f20"/><polygon points="28,0 166,0 196,22 28,22" fill="#231f20"/></svg>
    <span>About Us</span>
  </div>
  <p class="body-copy" style="top:136px">Bellhaven Court is one of Santa Monica's rare commercial properties that is both strategically located in the city's burgeoning central business district, yet ideally positioned on palm-lined Ocean Ave directly across from the Pacific Ocean. Built in 1987, the 3-story mixed-use commercial and retail property features prestigious retail Tenants such as Kelp Tavu and Dune Kitchen.</p>

  <div class="photo" role="img" aria-label="Photo of a balcony walkway with planters overlooking palms and the ocean" style="left:351px;top:133px;width:192px;height:290px;background:linear-gradient(180deg,#2a63c6 0%,#8fb4e2 35%,#c9c6bd 55%,#5f7b3a 80%,#3c4f2a 100%);border:1px solid #231f20"></div>

  <div class="tab" style="top:252px">
    <svg width="196" height="22" viewBox="0 0 196 22"><rect x="0" y="0" width="25" height="22" fill="#231f20"/><polygon points="28,0 166,0 196,22 28,22" fill="#231f20"/></svg>
    <span>Property Description</span>
  </div>
  <p class="body-copy" style="top:290px">A year-round coastal Mediterranean climate, a highly diverse business sector, and the vibrant, pedestrian-oriented Linden Row Walkway and Harbor Crest Arcade makes this beachside community a highly desirable commercial and retail location.</p>
  <ul class="bullets" style="left:34px;top:360px;width:220px">
    <li style="margin-bottom:14px">Rare Class A Oceanfront Office Space in the heart of Santa Monica.</li>
    <li>2nd Floor Office Space consisting of 16,159 square feet with private balconies.</li>
  </ul>

  <div class="tab" style="top:449px">
    <svg width="196" height="22" viewBox="0 0 196 22"><rect x="0" y="0" width="25" height="22" fill="#231f20"/><polygon points="28,0 166,0 196,22 28,22" fill="#231f20"/></svg>
    <span>Building Amenities</span>
  </div>
  <ul class="bullets" style="left:34px;top:490px;width:500px;line-height:21px">
    <li>Lorem ipsum dolor sit amet, consectetur adipiscing elit. Sed at ante.</li>
    <li>Lorem ipsum dolor sit amet, consectetur adipiscing elit. Sed at ante. Mauris eleifend, quam a vulputate dictum.</li>
    <li>Lorem ipsum dolor sit amet, consectetur adipiscing elit. Sed at ante. Mauris eleifend</li>
    <li>Lorem ipsum dolor sit amet, consectetur adipiscing elit. Sed at ante.</li>
    <li>Lorem ipsum dolor sit amet, consectetur adipiscing elit. Sed at ante. Mauris eleifend, quam a vulputate dictum.</li>
    <li>Lorem ipsum dolor sit amet, consectetur adipiscing elit. Sed at ante. Mauris eleifend, quam a vulputate dictum.</li>
  </ul>

  <div class="contact">
    <h3>Contact Us :</h3>
    <p>Verlinde Property.<br>5127 N Harlow Ave, Suite 210, West Hollywood, Ca. 90069, (310) 555-0142<br>www.verlindeproperty.com</p>
    <h3 class="gap">Our Leasing Agents :</h3>
    <p class="gap">Trevor L. Ashdown (310) 555-0142<br>trev@verlindeproperty.com</p>
    <p class="gap">Mark Oda (310) 555-0187<br>mark@verlindeproperty.com</p>
  </div>
  <div class="photo" role="img" aria-label="Photo of an elevator lobby with grey panels and red carpet" style="left:366px;top:634px;width:177px;height:134px;background:linear-gradient(180deg,#c9c9c9 0%,#6e7075 45%,#55575c 70%,#8e1c22 88%,#e2e2e2 100%)"></div>
</section>

</body>
</html>
```